Designing a billboard

Should have
Corwell & Pine, LLC
Ph: 512-647-3918
Auto Accidents / Personal Injury
Family Law
Criminal Defense
Real Estate
Free Consultation

Target Market(s)

Legal

Industry/Entity Type

Legal

Font styles to use
Serif
Sans Serif

Requirements
Must have
• Designing a billboard

Should have
Corwell & Pine, LLC
Ph: 512-647-3918
Family Law
Criminal Defense
Real Estate
Free Consultation
Nice to have
• Nice to have info above
Should not have
• None

```html
<!DOCTYPE html>
<html lang="en">
<head>
<meta charset="utf-8">
<title>Corwell &amp; Pine, LLC — Billboard</title>
<link href="https://fonts.googleapis.com/css2?family=EB+Garamond:ital,wght@0,600;1,400&family=Oswald:wght@500&family=Montserrat:wght@700;800&display=swap" rel="stylesheet">
<style>
  :root {
    --stage: #5c5c5c;
    --sand: #cdbd97;
    --sand-light: #dfd3b4;
    --brown: #8b6149;
    --brown-edge: #a57a5e;
    --ink: #22262b;
    --white: #ffffff;
    --photo-a: #9aa3a8;
    --photo-b: #6f7a84;
    --photo-c: #8a7f70;
  }
  html, body {
    margin: 0;
    width: 1046px;
    height: 1200px;
    overflow: hidden;
    background: var(--stage);
  }
  .billboard {
    position: absolute;
    left: 23px;
    top: 400px;
    width: 1000px;
    height: 400px;
    overflow: hidden;
    background: var(--sand);
    box-shadow: 0 14px 30px rgba(0,0,0,.45);
  }
  .billboard-shapes {
    position: absolute;
    inset: 0;
  }
  .firm-name {
    position: absolute;
    left: 46px;
    top: 12px;
    margin: 0;
    font-family: "EB Garamond", serif;
    font-weight: 600;
    font-size: 54px;
    line-height: 1;
    color: var(--ink);
    letter-spacing: .3px;
  }
  .attorneys {
    position: absolute;
    left: 104px;
    top: 90px;
    margin: 0;
    font-family: "EB Garamond", serif;
    font-style: italic;
    font-size: 20px;
    color: var(--ink);
  }
  .practice-areas {
    position: absolute;
    left: 46px;
    top: 148px;
    margin: 0;
    padding: 0;
    list-style: none;
    font-family: "Oswald", sans-serif;
    font-weight: 500;
    font-size: 25px;
    line-height: 41px;
    color: var(--white);
    text-transform: uppercase;
  }
  .practice-areas li { display: flex; }
  .practice-areas .area::before {
    content: "\00BB";
    margin-right: 10px;
    font-size: 28px;
  }
  .practice-areas .area + .area { margin-left: 42px; }
  .consult-pill {
    position: absolute;
    left: 49px;
    top: 273px;
    width: 473px;
    height: 44px;
    border-radius: 22px;
    background: var(--white);
    display: flex;
    align-items: center;
    justify-content: center;
    font-family: "Montserrat", sans-serif;
    font-weight: 800;
    font-size: 23px;
    letter-spacing: .4px;
    color: var(--brown);
  }
  .phone {
    position: absolute;
    left: 48px;
    top: 324px;
    display: flex;
    align-items: center;
    gap: 18px;
    font-family: "Montserrat", sans-serif;
    font-weight: 800;
    font-size: 50px;
    color: var(--ink);
    line-height: 1;
  }
  .phone-icon { width: 56px; height: 56px; }
</style>
</head>
<body>
  <section class="billboard">
    <svg class="billboard-shapes" viewBox="0 0 1000 400" width="1000" height="400">
      <defs>
        <linearGradient id="photoTone" x1="0" y1="0" x2="1" y2="1">
          <stop offset="0" stop-color="var(--photo-a)"/>
          <stop offset=".55" stop-color="var(--photo-b)"/>
          <stop offset="1" stop-color="var(--photo-c)"/>
        </linearGradient>
      </defs>
      <path class="swoosh" d="M508 0 L800 0 L740 108 Q705 140 650 122 Q598 104 560 40 Z" fill="var(--sand-light)"/>
      <path class="corner-accent" d="M0 290 L58 400 L0 400 Z" fill="var(--sand-light)"/>
      <rect class="services-band" x="0" y="130" width="640" height="163" fill="var(--brown)"/>
      <path class="photo-area" role="img" aria-label="Photo: two drivers on their phones beside two cars after a collision in a parking lot"
        d="M770 0 L1000 0 L1000 400 L615 400 L505 225 Q485 190 510 160 Q530 134 572 132 L660 132 Q700 132 725 95 L770 0 Z"
        fill="url(#photoTone)" stroke="var(--brown-edge)" stroke-width="5"/>
      <path class="corner-accent" d="M955 0 L1000 0 L1000 40 Z" fill="var(--sand-light)"/>
    </svg>

    <h1 class="firm-name">Corwell &amp; Pine, LLC</h1>
    <p class="attorneys">Attorneys: Evan Corwell, &amp; Daniel R. Pine</p>

    <ul class="practice-areas">
      <li><span class="area">Auto Accidents / Personal Injury</span></li>
      <li><span class="area">Family Law</span><span class="area">Real Estate</span></li>
      <li><span class="area">Criminal Defense</span></li>
    </ul>

    <div class="consult-pill">FOR FREE CONSULTATION</div>

    <div class="phone">
      <svg class="phone-icon" viewBox="0 0 56 56" aria-hidden="true">
        <circle cx="28" cy="28" r="24" fill="var(--white)" stroke="var(--brown)" stroke-width="6"/>
        <path d="M21 15 Q17 16 17 21 Q18 32 26 39 Q32 43 37 41 Q40 39 39 36 L35 32 Q33 31 31 33 L29 34 Q24 30 22 26 L23 24 Q25 22 24 20 Z" fill="var(--brown)"/>
      </svg>
      <span class="phone-number">(512) 647-3918</span>
    </div>
  </section>
</body>
</html>
```